Real estate company needs a letterhead design

A young real estate company needs a letterhead / stationery design, it should include the company's logo. It should look exactly the same as on the business cards. (With the phrase "a brand of KEV Wohnbau & Grundstücksentwicklung GmbH")

In addition, it should also include the 4 round seals.

color code blue # 00456b gray # 333333

Word and PDF are welcome.

KEV Wohnbau & Grundstücksentwicklung GmbH
Managing director: Mag. Lukas Fellnhuber
Matthias-Ortner-Strasse 3c / 41
6300 Wörgl

Tel .: +436648172093
Email: office@wohnglanz-beispiel.at
Web: www.wohnglanz-beispiel.at

Sparkasse Almtal, Bergländer Sparkasse from 1882, Genossenschaftskasse
Anton-Weissauer-Strasse 7, 6300 Wörgl
IBAN: AT31 4817 2964 0058 2316
BIC: GLMTAT44XXX
Account holder: KEV Wohnbau & Grundstücksentwicklung GmbH

FN: XXXXXXX
UID: XXXXXXX

```html
<!DOCTYPE html>
<html lang="de">
<head>
<meta charset="utf-8">
<title>Wohnglanz Briefpapier – Revision 1D</title>
<link rel="stylesheet" href="https://fonts.googleapis.com/css2?family=Open+Sans:wght@700;800&family=Poppins:wght@600;700&family=Source+Sans+3:ital,wght@0,400;0,600;0,700;1,600&display=swap">
<style>
  :root {
    --brand-blue: #00456b;
    --ink: #333333;
    --muted: #8b8b9b;
    --stage: #d4d5d7;
    --paper: #ffffff;
    --seal-red: #e3362b;
  }
  * { box-sizing: border-box; margin: 0; padding: 0; }
  html, body { width: 1200px; height: 1200px; overflow: hidden; }
  body {
    position: relative;
    background: var(--stage);
    font-family: "Source Sans 3", Arial, sans-serif;
    color: var(--ink);
  }
  .stage-title {
    position: absolute; top: 30px; left: 0; width: 1200px;
    text-align: center;
    font-family: "Open Sans", Arial, sans-serif;
    font-weight: 800; font-size: 43px; letter-spacing: 3px;
    color: var(--brand-blue);
  }
  .letterhead {
    position: absolute; left: 220px; top: 129px;
    width: 739px; height: 1040px;
    background: var(--paper);
    box-shadow: 0 2px 10px rgba(0,0,0,.18);
    overflow: hidden;
  }
  .header-bar {
    position: absolute; left: 0; top: 0; width: 25px; height: 113px;
    background: var(--brand-blue);
  }
  .brand-name {
    position: absolute; left: 40px; top: 42px;
    font-family: "Open Sans", Arial, sans-serif;
    font-weight: 800; font-size: 46px; line-height: 1;
    color: var(--brand-blue);
  }
  .brand-tagline {
    position: absolute; left: 40px; top: 103px;
    font-style: italic; font-weight: 600; font-size: 11px;
    color: var(--ink);
  }
  .header-rule {
    position: absolute; left: 353px; right: 0; top: 109px;
    height: 2px; background: var(--brand-blue);
  }
  .seals { position: absolute; left: 0; top: 0; }
  .recipient {
    position: absolute; left: 33px; top: 206px;
    font-size: 12.5px; line-height: 16px; color: #444;
  }
  .recipient-name {
    font-family: "Poppins", Arial, sans-serif;
    font-weight: 700; font-size: 15px; letter-spacing: .8px;
    color: var(--brand-blue); line-height: 20px;
  }
  .recipient b { color: var(--ink); }
  .letter-date {
    position: absolute; right: 32px; top: 262px;
    font-size: 12.5px; color: #444;
  }
  .letter-date b {
    font-family: "Poppins", Arial, sans-serif; font-weight: 600;
    color: var(--brand-blue); font-size: 11.5px;
  }
  .letter-body {
    position: absolute; left: 33px; top: 334px; width: 676px;
    font-size: 11.6px; line-height: 15.9px; text-align: justify;
  }
  .letter-body p { margin-bottom: 15.9px; }
  .letter-body .muted { color: var(--muted); }
  .letter-body .strong { color: var(--ink); }
  .signature {
    position: absolute; left: 68px; top: 755px; width: 182px;
    text-align: center;
  }
  .signature-mark {
    display: block; width: 170px; height: 26px; margin: 0 auto 10px;
    background: linear-gradient(90deg, #e9e9ec, #dcdce0);
    border-radius: 3px;
  }
  .signature-line { height: 1px; background: var(--ink); }
  .signature-role { margin-top: 10px; font-size: 12px; letter-spacing: .4px; }
  .footer {
    position: absolute; left: 0; bottom: 0; width: 100%; height: 122px;
    background: var(--brand-blue); color: #fff;
    font-size: 8px; line-height: 12px;
  }
  .footer-col { position: absolute; top: 20px; }
  .footer-col p + p { margin-top: 5px; }
  .footer-company { left: 33px; }
  .footer-company h2 { font-size: 9.2px; font-weight: 700; margin-bottom: 6px; }
  .footer-contact { left: 256px; }
  .footer-bank { left: 387px; }
  .footer-register { left: 654px; }
  .footer b { font-weight: 700; }
</style>
</head>
<body>
  <h1 class="stage-title">REVISION - MOCKUP 1D</h1>

  <main class="letterhead">
    <div class="header-bar"></div>
    <div class="brand-name">WOHNGLANZ</div>
    <div class="brand-tagline">eine Marke der KEV Wohnbau &amp; Grundstücksentwicklung GmbH</div>
    <div class="header-rule"></div>

    <svg class="seals" width="739" height="120" viewBox="0 0 739 120" aria-label="Vier Gütesiegel">
      <g fill="#fff" stroke="var(--seal-red)" stroke-width="1.3">
        <circle cx="444" cy="60" r="35"/>
        <circle cx="523" cy="60" r="35"/>
        <circle cx="602" cy="60" r="35"/>
        <circle cx="687" cy="60" r="35"/>
      </g>
      <g fill="var(--seal-red)">
        <circle cx="444" cy="60" r="21"/>
        <circle cx="523" cy="60" r="21"/>
        <circle cx="602" cy="60" r="21"/>
        <circle cx="687" cy="60" r="21"/>
      </g>
    </svg>

    <div class="recipient">
      <div>To</div>
      <div class="recipient-name">Tom Berger</div>
      <div>CEO, NORDWERK STUDIO</div>
      <div><b>W:</b> www.nordwerk-beispiel.com</div>
    </div>
    <div class="letter-date"><b>Date:</b> 24-03-2018</div>

    <section class="letter-body">
      <p class="muted">Lorem ipsum dolor sit amet, consectetur adipiscing elit. Pellentesque dictum, ante non ullamcorp er convallis, nunc quam blandit metus, ac mollis eros felis a orci. Donec congue, mauris ut pulvinar lobortis, dolor massa feugiat nisi, at tincidunt metus leo vel elit. Proin facilisis semper lobortis. Vivamus augue purus, cursus quis urna non, accumsan pellentesque est. Nulla in iaculis magna, quis aliqu et ex. Cras efficitur metus eget purus euismod facilisis. Proin non metus tincidunt, auctor ipsum a, tempor mi.</p>
      <p class="strong">Nulla egestas vulputate risus, ut vestibulum diam commodo id. Mauris ornare libero eu erat portt itor ultrices. Proin sed lectus scelerisque ligula bibendum sagittis ac nec leo. Donec ac accumsan diam, et lobortis mauris.</p>
      <p class="strong">Nulla congue volutpat nisl ac lobortis. Integer dignissim interdum libero, quis feugiat velit pretium at. Phasellus sit amet libero rutrum, feugiat odio et, tempus purus. Cras ultricies, leo at fringilla solli cit udin, leo sapien placerat enim, a rutrum lorem enim ut tortor. Phasellus magna ante, cong ue maximus egestas sit amet, venenatis scelerisque felis.</p>
      <p class="muted">Nulla congue volutpat nisl ac lobortis. Integer dignissim interdum libero, quis feugiat velit pretium at. Phasellus sit amet libero rutrum, feugiat odio et, tempus purus. Cras ultricies, leo at fringilla solli cit udin, leo sapien placerat enim, a rutrum lorem enim ut tortor. Phasellus magna ante, cong ue maximus egestas sit amet, venenatis scelerisque felis.</p>
      <p class="muted">Curabitur vitae urna volutpat, varius velit vehicula, fermentum magna. In maximus metus nunc, nec aliquet justo commodo eget. Nullam rhoncus vehicula gravida. Maecenas non sem at erat lacinia con vallis. Aliquam at lobortis erat.</p>
      <p class="muted">Nulla congue volutpat nisl ac lobortis. Integer dignissim interdum libero, quis feugiat velit pretium at. Phasellus sit amet libero rutrum, feugiat odio et, tempus purus. Cras ultricies, leo at fringilla solli cit udin, leo sapien placerat enim, a rutrum lorem enim ut tortor. Phasellus magna ante, cong ue maximus egestas sit amet, venenatis scelerisque felis</p>
    </section>

    <div class="signature">
      <span class="signature-mark" role="img" aria-label="Handschriftliche Unterschrift von Mag. Lukas Fellnhuber"></span>
      <div class="signature-line"></div>
      <div class="signature-role">Geschäftsführer</div>
    </div>

    <footer class="footer">
      <div class="footer-col footer-company">
        <h2>KEV Wohnbau &amp; Grundstücksentwicklung GmbH</h2>
        <p>Mag. Lukas Fellnhuber<br>Geschäftsführer</p>
        <p>Matthias-Ortner-Strasse 3c / 41<br>6300 Wörgl</p>
      </div>
      <div class="footer-col footer-contact">
        <p><b>Tel:</b> +436648172093<br><b>Email:</b> office@wohnglanz-beispiel.at<br><b>Web:</b> www.wohnglanz-beispiel.at</p>
      </div>
      <div class="footer-col footer-bank">
        <p>Sparkasse Almtal, Bergländer Sparkasse from 1882, Genossenschaftskasse<br>Anton-Weissauer-Strasse 7, 6300 Wörgl</p>
        <p><b>IBAN:</b> AT31 4817 2964 0058 2316<br><b>BIC:</b> GLMTAT44XXX<br><b>Kontoinhaber :</b> KEV Wohnbau &amp; Grundstücksentwicklung GmbH</p>
      </div>
      <div class="footer-col footer-register">
        <p><b>FN:</b> XXXXXXX<br><b>UID:</b> XXXXXXX</p>
      </div>
    </footer>
  </main>
</body>
</html>
```